Online Marketplace Startup for Community Facilities (Tovaroom)

A innovative, modern website design is required for a new startup called Tovaroom. Tovaroom will be an online marketplace for searching for and booking community facilities, such as schools facilities (sports grounds, halls, classrooms etc.), churches, hospitals and other community facilities.

The attached brief has been created to provide guidance on the structure and content required.

The web design shall feature a modern, innovative but user friendly interface similar style to other web start up pages:
www.hallquiver.co.uk
www.vendlark.com.au
www.artfennel.com.au

The web design shall be ‘wordpress’ compliant and allow for future functionality to be added and coded (e.g. animations, flash, blogs etc) and content to be editable.

The following brief has been created to provide guidance on the structure and content required.

An existing logo developed for Tovaroom shall be utilised and incorporated in the top left hand cover of the cover landing page (refer to attached logo designs).

Refer to attached 'Website brief' for more details on requirements.
Updates

Project Deadline Extended
Reason: I wish to grant an extension to the deadline to provide designers with more time to submit their designs.

Target Market(s)

TovaRoom will focus on building a customer network of both community facility owners (schools, hospitals, churches) and hirers (non-government organisations, community groups, event management companies, commercial businesses). Members of the general public will also be encouraged to book facilities for private functions.

Industry/Entity Type

Community

Coding

Coded - Design and coding required

Number of Pages Required

5+ page

Font styles to use
Sans Serif

Colors
3176b5
ffffff
85cae6
33a6d7

Requirements
Must have
• The web design shall feature a modern, innovative but user friendly interface similar style to other web start up pages:
• www.hallquiver.co.uk
• www.vendlark.com.au
• www.artfennel.com.au
• The web design shall be ‘wordpress’ compliant and allow for future functionality to be added and coded (e.g. animations, flash, blogs etc) and content to be editable.
• Refer to Project brief for other requirements
Nice to have
• Refer to Project brief
Should not have
• Refer to Project brief

```html
<!DOCTYPE html>
<html lang="en">
<head>
<meta charset="utf-8">
<title>TovaRoom – Community Facility Marketplace</title>
<link rel="stylesheet" href="https://fonts.googleapis.com/css2?family=Poppins:wght@400;500&family=Arvo:wght@700&display=swap">
<style>
  :root {
    --brand-blue: #1f4a8a;
    --nav-text: #4a4a4a;
    --nav-active: #1f4a8a;
    --social-grey: #8a8a8a;
    --header-bg: #ffffff;
    --hero-deep: #3e5f93;
    --hero-mid: #5b7cb0;
    --hero-light: #7f9cc8;
    --hero-text: #ffffff;
    --cta-bg: #f0646f;
    --cta-text: #ffffff;
    --dot-ring: #dfe6f1;
  }
  * { margin: 0; padding: 0; box-sizing: border-box; }
  html, body { width: 1200px; height: 452px; overflow: hidden; background: #ffffff; }
  body { font-family: "Poppins", Arial, sans-serif; }

  .page { position: relative; width: 1200px; height: 452px; }

  .site-header {
    position: absolute; left: 0; top: 0; width: 1200px; height: 71px;
    background: var(--header-bg);
  }
  .brand {
    position: absolute; left: 94px; top: 22px;
    display: flex; align-items: center; gap: 8px;
    font-family: "Poppins", Arial, sans-serif; font-weight: 500;
    font-size: 26px; line-height: 1; color: var(--brand-blue);
  }
  .brand-dot { width: 22px; height: 22px; border-radius: 50%; background: var(--brand-blue); }

  .main-nav { position: absolute; top: 33px; left: 0; }
  .main-nav a {
    position: absolute; white-space: nowrap; text-decoration: none;
    font-size: 12.5px; color: var(--nav-text); line-height: 1;
  }
  .main-nav a.is-active { color: var(--nav-active); padding-bottom: 4px; border-bottom: 1px solid var(--nav-active); }

  .social-links { position: absolute; top: 35px; left: 1036px; display: flex; gap: 11px; }
  .social-links span { width: 11px; height: 11px; border-radius: 2px; background: var(--social-grey); display: block; }

  .hero {
    position: absolute; left: 0; top: 71px; width: 1200px; height: 381px;
    border-top: 1px solid #6f7f96;
  }
  .hero-photo {
    position: absolute; inset: 0;
    background:
      radial-gradient(ellipse 380px 300px at 230px 200px, #33507f 0%, rgba(51,80,127,0) 100%),
      radial-gradient(ellipse 360px 260px at 1050px 150px, #9ab3d6 0%, rgba(154,179,214,0) 100%),
      linear-gradient(100deg, var(--hero-deep) 0%, var(--hero-mid) 55%, var(--hero-light) 100%);
  }
  .hero-title {
    position: absolute; left: 0; width: 1200px; top: 140px;
    text-align: center; font-family: "Arvo", Georgia, serif; font-weight: 700;
    font-size: 29px; line-height: 37px; color: var(--hero-text);
  }
  .hero-cta {
    position: absolute; left: 536px; top: 245px; width: 132px; height: 35px;
    background: var(--cta-bg); color: var(--cta-text);
    font-size: 13px; line-height: 35px; text-align: center; text-decoration: none;
  }
  .slide-dots { position: absolute; left: 1158px; top: 168px; display: flex; flex-direction: column; gap: 15px; }
  .slide-dots span { width: 9px; height: 9px; border-radius: 50%; border: 1.5px solid var(--dot-ring); display: block; }
</style>
</head>
<body>
<div class="page">
  <header class="site-header">
    <div class="brand"><span class="brand-dot"></span>TovaRoom</div>
    <nav class="main-nav">
      <a class="is-active" style="left:336px">Home</a>
      <a style="left:394px">About Us</a>
      <a style="left:470px">How it Works</a>
      <a style="left:567px">Services</a>
      <a style="left:639px">Packages</a>
      <a style="left:719px">Why Tovaroom?</a>
      <a style="left:846px">News</a>
      <a style="left:901px">FAQ</a>
      <a style="left:948px">Contact Us</a>
    </nav>
    <div class="social-links" aria-label="Social links">
      <span></span><span></span><span></span><span></span>
    </div>
  </header>

  <section class="hero">
    <div class="hero-photo" role="img" aria-label="Photo of a hand writing with a pen over a financial line chart, tinted blue"></div>
    <h1 class="hero-title">Utilising your facility to create value for<br>your organisation and the community.</h1>
    <a class="hero-cta">Get Started</a>
    <div class="slide-dots">
      <span></span><span></span><span></span><span></span><span></span>
    </div>
  </section>
</div>
</body>
</html>
```